Q827 PowerPoint Presentation

As you can see the design of this PowerPoint isn't cohesive. There are a lot of images and words that give it a very jumbled and busy appeal. We want to turn this into a sharp, cohesive and visually appealing presentation without taking away too much of the information. Feel free to use the images to create your own artwork for the PowerPoint.

Please don't hesitate to contact me with any questions.

```html
<!DOCTYPE html>
<html lang="en">
<head>
<meta charset="utf-8">
<title>Q827 – Architecture Decision Analytics</title>
<link href="https://fonts.googleapis.com/css2?family=Roboto:wght@300;400;700&family=Roboto+Condensed:wght@700&display=swap" rel="stylesheet">
<style>
  :root{
    --band-top:#0f5797;
    --blue-main:#0b5fa5;
    --blue-logo:#0d5fa8;
    --yellow:#f5c400;
    --white:#ffffff;
    --grey-text:#6b6b6b;
    --grey-light:#f3f3f3;
    --grey-dark:#dedede;
    --foot-1:#5b8fc4;
    --foot-2:#0a7cc0;
    --foot-3:#0a6bb2;
    --foot-4:#0f589c;
    --foot-5:#0c4a85;
  }
  *{margin:0;padding:0;box-sizing:border-box}
  html,body{width:1200px;height:833px;overflow:hidden}
  body{font-family:"Roboto",Arial,sans-serif;background:var(--white);position:relative}

  .top-band{position:absolute;left:0;top:0;width:1200px;height:30px;background:var(--band-top)}

  .header{position:absolute;left:0;top:30px;width:1200px;height:70px;background:var(--white)}
  .brand{position:absolute;left:42px;top:16px;display:flex;align-items:center;gap:10px}
  .brand-dot{width:36px;height:36px;border-radius:50%;background:var(--blue-logo)}
  .brand-name{font-size:34px;font-weight:700;color:var(--blue-logo);letter-spacing:-0.5px}
  .brand-tagline{font-size:32px;font-weight:300;color:var(--grey-text);margin-left:8px}
  .partner{position:absolute;right:38px;top:24px;display:flex;align-items:center;gap:8px}
  .partner-dot{width:10px;height:10px;border-radius:50%;background:var(--blue-logo)}
  .partner-name{font-size:20px;font-weight:700;color:var(--blue-logo)}

  .hero{position:absolute;left:0;top:100px;width:1200px;height:417px;background:var(--blue-main);color:var(--white)}
  .hero-kicker{position:absolute;left:0;top:56px;width:1200px;text-align:center;font-size:35px;font-weight:300}
  .hero-title{position:absolute;left:0;top:90px;width:1200px;text-align:center;font-size:53px;font-weight:300}

  .flow-arcs{position:absolute;left:0;top:0;width:1200px;height:417px}

  .step{position:absolute;top:180px;width:275px}
  .step-icon{height:58px;display:block}
  .step-title{font-family:"Roboto Condensed",Arial,sans-serif;font-weight:700;font-size:30px;margin-top:6px;line-height:36px}
  .step-text{font-size:13px;font-weight:700;line-height:17.5px;margin-top:14px}
  .step--challenge{left:134px}
  .step--need{left:511px}
  .step--result{left:839px}

  .gallery{position:absolute;left:0;top:517px;width:1200px;height:269px;background:linear-gradient(var(--grey-light),var(--grey-dark))}
  .shot{position:absolute;top:55px;width:219px;height:161px;background:var(--white);box-shadow:0 2px 5px rgba(0,0,0,.25);padding:16px 15px 13px}
  .shot-screen{width:100%;height:100%;border:1px solid #9a9a9a}
  .shot--map{left:175px}
  .shot--map .shot-screen{background:linear-gradient(135deg,#e9d6c8,#7e8a9a 45%,#e2b04a 70%,#c9ccd2)}
  .shot--dash{left:488px}
  .shot--dash .shot-screen{background:linear-gradient(90deg,#dfe7f0 0 33%,#f06aa6 33% 62%,#eef2f7 62%)}
  .shot--bars{left:800px}
  .shot--bars .shot-screen{background:linear-gradient(#f4f4f4 0 22%,#4e82b8 22% 92%,#f4f4f4 92%)}

  .footer{position:absolute;left:0;top:786px;width:1200px;height:47px;display:flex}
  .footer-seg{width:240px;height:100%}
  .footer-seg:nth-child(1){background:var(--foot-1)}
  .footer-seg:nth-child(2){background:var(--foot-2)}
  .footer-seg:nth-child(3){background:var(--foot-3)}
  .footer-seg:nth-child(4){background:var(--foot-4)}
  .footer-seg:nth-child(5){background:var(--foot-5)}
  .footer-copy,.footer-url{position:absolute;top:13px;font-size:17px;color:var(--white)}
  .footer-copy{left:16px}
  .footer-url{right:12px}
</style>
</head>
<body>
  <div class="top-band"></div>

  <header class="header">
    <div class="brand">
      <span class="brand-dot"></span>
      <span class="brand-name">Q827</span>
      <span class="brand-tagline">Idea to Reality</span>
    </div>
    <div class="partner">
      <span class="partner-dot"></span>
      <span class="partner-name">Kestrelworks</span>
    </div>
  </header>

  <section class="hero">
    <p class="hero-kicker">A Web-Based Environment for</p>
    <h1 class="hero-title">Architecture Decision Analytics</h1>

    <svg class="flow-arcs" viewBox="0 0 1200 417">
      <defs>
        <marker id="arrowhead" markerWidth="8" markerHeight="8" refX="4" refY="4" orient="auto">
          <path d="M0,0 L8,4 L0,8 Z" fill="#f5c400"/>
        </marker>
      </defs>
      <path d="M278,240 Q380,120 484,246" fill="none" stroke="#f5c400" stroke-width="3.5" marker-end="url(#arrowhead)"/>
      <path d="M610,240 Q712,120 814,246" fill="none" stroke="#f5c400" stroke-width="3.5" marker-end="url(#arrowhead)"/>
    </svg>

    <div class="step step--challenge">
      <svg class="step-icon" width="70" height="58" viewBox="0 0 70 58">
        <g fill="#f5c400">
          <circle cx="25" cy="14" r="11"/><circle cx="40" cy="10" r="10"/><circle cx="52" cy="17" r="10"/>
          <rect x="18" y="14" width="42" height="14" rx="7"/>
          <circle cx="5" cy="26" r="3"/><circle cx="12" cy="24" r="4"/>
        </g>
        <g stroke="#f5c400" stroke-width="2">
          <line x1="31" y1="28" x2="31" y2="58"/><line x1="40" y1="28" x2="40" y2="58"/>
          <line x1="31" y1="35" x2="40" y2="35"/><line x1="31" y1="42" x2="40" y2="42"/>
          <line x1="31" y1="49" x2="40" y2="49"/><line x1="31" y1="56" x2="40" y2="56"/>
        </g>
      </svg>
      <h2 class="step-title">The Challenge</h2>
      <p class="step-text">Identifying / integrating An organizations “sources of record” information and making it readily available (assets, budget, systems, references).</p>
    </div>

    <div class="step step--need">
      <svg class="step-icon" width="50" height="58" viewBox="0 0 50 58">
        <g fill="#f5c400">
          <rect x="14" y="2" width="24" height="18" rx="2"/>
          <rect x="0" y="48" width="12" height="8"/><rect x="19" y="48" width="12" height="8"/><rect x="38" y="48" width="12" height="8"/>
        </g>
        <rect x="17" y="5" width="18" height="11" fill="#0b5fa5"/>
        <g stroke="#f5c400" stroke-width="2.5" fill="none">
          <path d="M25,20 V34 M6,48 V38 H44 V48 M25,34 V48"/>
        </g>
      </svg>
      <h2 class="step-title">The Need</h2>
      <p class="step-text">A portal solution enabling the rapid ingestion, organization, integration, display and analysis of data from multiple sources.</p>
    </div>

    <div class="step step--result">
      <svg class="step-icon" width="70" height="66" viewBox="0 0 70 66" style="margin-top:-8px;height:66px">
        <g fill="none" stroke="#f5c400">
          <circle cx="28" cy="38" r="25" stroke-width="5"/>
          <circle cx="28" cy="38" r="14" stroke-width="5"/>
        </g>
        <circle cx="28" cy="38" r="4" fill="#f5c400"/>
        <line x1="28" y1="38" x2="58" y2="8" stroke="#f5c400" stroke-width="3"/>
        <path d="M52,4 L62,0 L58,10 L68,12 L58,16 L54,10 Z" fill="#f5c400"/>
      </svg>
      <h2 class="step-title">The Result</h2>
      <p class="step-text">A collaborative architecture decision support tool that allows users to associate mission guidance with mission execution</p>
    </div>
  </section>

  <section class="gallery">
    <figure class="shot shot--map"><div class="shot-screen" role="img" aria-label="Application screenshot with four US maps showing counts by state"></div></figure>
    <figure class="shot shot--dash"><div class="shot-screen" role="img" aria-label="Application screenshot with strategic plans, agency initiatives, a pie chart and a bar chart"></div></figure>
    <figure class="shot shot--bars"><div class="shot-screen" role="img" aria-label="Application screenshot with a bar chart of products over time"></div></figure>
  </section>

  <footer class="footer">
    <div class="footer-seg"></div><div class="footer-seg"></div><div class="footer-seg"></div><div class="footer-seg"></div><div class="footer-seg"></div>
    <span class="footer-copy">© 2014 kestrelworks</span>
    <span class="footer-url">https://www.kestrelworks.com</span>
  </footer>
</body>
</html>
```